Website for Outdoor Furniture, Sunroom and life style design

I need a website for a company that creates sunroom furniture and design. A sunroom is a room within your home that is surrounded by windows to make it feel like you are outdoors while being indoors to protect you from weather and keep your comfortable.<br/><br/>The company designs and decorates sun rooms for home owners who want to relax and have the feeling of outdoors, while being indoors.

Target Market(s)

home owners, 40+ demographic

Number of Pages Required

5+ page

Requirements
Must have
• See attached zip files for more information including images, copy and descriptions.
• **CONTACT ONLY FROM PIXELBAZAR.COM ALL OTHER FORMS OF COMMUNICATION WILL BE IGNORED**
• COLORS: colors that compliment our logo which is attached here
• Clean, streamlined, easy to navigate.
• No clutter, flashing, bouncing, pop ups.
• Contact info on every page - phone, email, address, hours. Google map somewhere.
• Videos on every page relevant to the content
• Our products are sunrooms and shade but we consider ourselves to be selling a lifestyle. Outdoor living and design.
• Would like to incorporate images of people in our 40 plus demographic to reinforce the lifestyle theme.
• We need the following pages designed (Please see attached zip file for images and sample copy)
• 1. Home: Home page to have prominent area for updating current info like holiday hours, sales, new products, etc
• 2. Sunrooms: See attached zip file for images, text copy etc....
• 3. Shade Solutions: See attached zip file for images, text copy etc....
• 4. Options & Accessories: See attached zip file for images, text copy etc....
• 5. About Us: See attached zip file for images, text copy etc....
• Customer comments/reviews to appear in “bubbles” throughout site
Should not have
• - No search bar
• - No clutter, flashing, bouncing, pop ups.

```html
<!DOCTYPE html>
<html lang="en">
<head>
<meta charset="utf-8">
<title>Brightwell Rooms</title>
<link rel="stylesheet" href="https://fonts.googleapis.com/css2?family=Source+Sans+3:wght@400;600&display=swap">
<style>
:root{
  --accent:#e0622a;
  --accent-light:#eda130;
  --ink:#2b2b2b;
  --muted:#444;
  --band:#f0f0f0;
  --footer:#232323;
  --footer-bottom:#1b1b1b;
  --footer-text:#d6d6d6;
  --line:#3a3a3a;
}
*{margin:0;padding:0;box-sizing:border-box}
html,body{width:1200px;height:2848px;overflow:hidden}
body{position:relative;font-family:'Source Sans 3',sans-serif;color:var(--ink);background:#fff}
.abs{position:absolute}
.header{top:0;left:0;width:1200px;height:93px;background:#fff;border-bottom:1px solid #e4e4e4}
.brand{left:100px;top:30px}
.brand-name{font-size:26px;font-weight:600;color:var(--ink);line-height:1}
.nav{right:100px;top:36px;display:flex;gap:35px;font-size:15px}
.nav a{color:var(--ink);text-decoration:none;padding-bottom:4px}
.nav a.active{border-bottom:2px solid var(--accent)}
.photo{display:block}
.hero{top:93px;left:0;width:1200px;height:530px;background:linear-gradient(180deg,#8fa9dd 0%,#c9d3de 45%,#a99a86 80%,#6b5b4a 100%)}
.slide-arrow{width:42px;height:42px;border:2px solid #fff;border-radius:50%}
.tile{top:632px;height:472px;width:600px}
.tile-sun{left:0;background:linear-gradient(160deg,#5d8fc4,#9cc3e6 55%,#3a5a4a)}
.tile-shade{left:600px;background:linear-gradient(170deg,#8a5a3e,#cfd9c8 40%,#6f8d4a 70%,#5a4f4a)}
.badge{border-radius:50%;background:linear-gradient(200deg,#d4512a 0%,#e36b2b 55%,var(--accent-light) 100%);color:#fff;display:flex;flex-direction:column;align-items:center;justify-content:center;text-align:center;box-shadow:0 3px 8px rgba(0,0,0,.25)}
.badge .title{font-size:30px;line-height:1.05}
.badge .link{font-size:13px;margin-top:8px}
.projects{top:1104px;left:0;width:1200px;height:441px;background:var(--band)}
.section-title{width:1200px;left:0;text-align:center;font-size:29px;font-weight:600;color:var(--ink)}
.thumb{width:257px;height:254px;background:#fff;padding:4px;top:1237px}
.thumb div{width:100%;height:100%}
.ring{width:40px;height:40px;border:2px solid #444;border-radius:50%}
.about-text{left:100px;top:1770px;width:430px;font-size:13.5px;line-height:20.6px;color:var(--muted)}
.about-link{left:98px;top:1969px;font-size:13.5px;color:var(--accent)}
.about-photo{left:600px;top:1556px;width:600px;height:472px;background:linear-gradient(180deg,#2f5a1e,#4f7d2d 45%,#6e6a78 65%,#5b5b5e 100%)}
.offer{top:2036px;left:0;width:1200px;height:384px;background:var(--band)}
.offer-col{top:2158px;width:300px;text-align:center}
.offer-col svg{display:block;margin:0 auto}
.offer-col h3{font-size:23px;font-weight:400;margin-top:14px;color:var(--ink)}
.offer-col p{font-size:13.5px;line-height:22px;color:var(--muted);margin-top:8px;padding:0 20px}
.footer{top:2425px;left:0;width:1200px;height:351px;background:var(--footer)}
.foot-h{font-size:14px;font-weight:600;color:#fff;top:2474px}
.foot-h::after{content:"";display:block;width:52px;height:3px;background:var(--accent);margin-top:7px}
.contact-row{left:100px;display:flex;align-items:center;font-size:13px;color:var(--footer-text)}
.contact-row svg{width:16px;margin-right:10px}
.contact-row span{border-left:1px solid #555;padding-left:11px}
.social{left:100px;top:2664px;display:flex;gap:14px}
.social i{display:block;width:24px;height:24px;border-radius:50%;background:#8a8a8a}
.map{left:490px;top:2520px;width:288px;height:191px;background:linear-gradient(90deg,#ececec 70%,#cbe8cf 100%)}
.sitemap{left:875px;top:2510px;width:230px;list-style:none}
.sitemap li{font-size:12px;color:var(--footer-text);height:40.5px;line-height:40.5px;border-bottom:1px solid var(--line)}
.sitemap li:last-child{border-bottom:none}
.bottom{top:2776px;left:0;width:1200px;height:72px;background:var(--footer-bottom)}
.copy{left:100px;top:2801px;font-size:12px;color:#9a9a9a}
.copy b{color:#fff;font-weight:400}
.to-top{left:1062px;top:2789px;width:36px;height:36px;border:2px solid #9a9a9a;border-radius:50%}
</style>
</head>
<body>

<header class="abs header">
  <div class="abs brand"><div class="brand-name">Brightwell Rooms</div></div>
  <nav class="abs nav">
    <a class="active">Home</a><a>Sunrooms</a><a>Shade Solutions</a><a>Options &amp; Accessories</a><a>About Us</a>
  </nav>
</header>

<div class="abs photo hero" role="img" aria-label="Modern rooftop patio with white umbrellas, striped lounge seating and glass doors"></div>
<svg class="abs slide-arrow" style="left:16px;top:336px" viewBox="0 0 42 42"><path d="M24 13 L16 21 L24 29" fill="none" stroke="#fff" stroke-width="2"/></svg>
<svg class="abs slide-arrow" style="left:1143px;top:336px" viewBox="0 0 42 42"><path d="M18 13 L26 21 L18 29" fill="none" stroke="#fff" stroke-width="2"/></svg>

<div class="abs tile tile-sun" role="img" aria-label="Glass sunroom roof against a blue sky"></div>
<div class="abs tile tile-shade" role="img" aria-label="Wooden pergola over a deck with wicker lounge furniture"></div>
<div class="abs badge" style="left:384px;top:892px;width:179px;height:179px"><div class="title">Sunrooms</div><div class="link">View Details</div></div>
<div class="abs badge" style="left:987px;top:892px;width:179px;height:179px"><div class="title">Shade<br>Solutions</div><div class="link">View Details</div></div>

<section class="abs projects"></section>
<h2 class="abs section-title" style="top:1158px">Recent Projects</h2>
<svg class="abs ring" style="left:98px;top:1343px" viewBox="0 0 40 40"><path d="M23 12 L15 20 L23 28" fill="none" stroke="#444" stroke-width="2"/></svg>
<div class="abs thumb" style="left:185px"><div role="img" aria-label="Patio cover over a backyard deck" style="background:linear-gradient(160deg,#c9c2a6,#eeeeea 45%,#a0693f)"></div></div>
<div class="abs thumb" style="left:472px"><div role="img" aria-label="Covered porch with garden beds" style="background:linear-gradient(180deg,#dfe7ee,#f2f2ee 35%,#9b8a5a 70%,#6e9a3e)"></div></div>
<div class="abs thumb" style="left:761px"><div role="img" aria-label="Rattan chairs on a tiled floor" style="background:linear-gradient(180deg,#6b4a30,#8a5a34 50%,#5d5652)"></div></div>
<svg class="abs ring" style="left:1058px;top:1343px" viewBox="0 0 40 40"><path d="M17 12 L25 20 L17 28" fill="none" stroke="#444" stroke-width="2"/></svg>

<div class="abs badge" style="left:89px;top:1587px;width:162px;height:162px"><div class="title" style="font-size:29px">Who<br>We Are</div></div>
<p class="abs about-text">We carry a range of sunroom products, from screen rooms to 3 season sunrooms to all season sunrooms. We call ourselves the Lakeview Sunroom Experts quite simply because we specialize in sunrooms and sunroom related merchandise and we've been doing it for 30+ years. We don't do windows, doors, siding and roofing with sunrooms on the side. This is what sets us apart from our competitors, our experience and our focus on this particular home renovation category. Let us create a sunroom as individual as you are so that you can start enjoying summer on your terms, not Mother Natures’.</p>
<a class="abs about-link">Contact Us</a>
<div class="abs about-photo" role="img" aria-label="Wicker outdoor sofa set with cream cushions before a green hedge"></div>

<section class="abs offer"></section>
<h2 class="abs section-title" style="top:2091px">What We Offer</h2>
<div class="abs offer-col" style="left:85px">
  <svg width="90" height="78" viewBox="0 0 90 78" fill="none" stroke="#555" stroke-width="2"><path d="M4 12 L86 12 L70 22 L4 22 Z"/><path d="M8 22 V74 M64 22 V74 M8 74 H64"/><path d="M14 28 H58 M14 36 H58 M14 44 H58 M14 52 H58 M14 60 H58 M14 68 H58"/></svg>
  <h3>Architecture Design</h3>
  <p>Lorem Ipsum is simply dummy text of the printing and typesetting industry. Lorem Ipsum has been the industry.</p>
</div>
<div class="abs offer-col" style="left:447px">
  <svg width="90" height="78" viewBox="0 0 90 78" fill="none" stroke="#555" stroke-width="2"><path d="M16 14 H62 V58 H16 Z"/><path d="M62 30 H76 L86 42 V58 H62"/><circle cx="28" cy="62" r="6"/><circle cx="74" cy="62" r="6"/><path d="M2 30 H14 M6 40 H14 M2 50 H14"/></svg>
  <h3>Quick Delivery</h3>
  <p>Lorem Ipsum is simply dummy text of the printing and typesetting industry. Lorem Ipsum has been the industr.</p>
</div>
<div class="abs offer-col" style="left:821px">
  <svg width="90" height="78" viewBox="0 0 90 78" fill="none" stroke="#555" stroke-width="2"><circle cx="30" cy="26" r="18"/><circle cx="30" cy="26" r="7"/><path d="M44 38 L78 70 L70 76 L38 44"/></svg>
  <h3>Installation</h3>
  <p>Lorem Ipsum is simply dummy text of the printing and typesetting industry. Lorem Ipsum has been the industry.</p>
</div>

<footer class="abs footer"></footer>
<h4 class="abs foot-h" style="left:100px">CONTACT DETAILS</h4>
<div class="abs contact-row" style="top:2524px"><svg viewBox="0 0 16 16"><path d="M3 1 L6 1 L7 5 L5 6 Q6 9 10 11 L11 9 L15 10 L15 13 Q14 15 12 15 Q2 13 1 3 Q1 1 3 1Z" fill="#8a8a8a"/></svg><span>555 010 4821</span></div>
<div class="abs contact-row" style="top:2562px"><svg viewBox="0 0 16 16"><path d="M8 1 A5 5 0 0 1 13 6 C13 10 8 15 8 15 C8 15 3 10 3 6 A5 5 0 0 1 8 1Z" fill="#8a8a8a"/><circle cx="8" cy="6" r="2" fill="#232323"/></svg><span>14 Harbour Lane, Lakeview, Ontario</span></div>
<div class="abs contact-row" style="top:2600px"><svg viewBox="0 0 16 16"><rect x="1" y="3" width="14" height="10" fill="#8a8a8a"/><path d="M1 3 L8 9 L15 3" fill="none" stroke="#232323" stroke-width="1.2"/></svg><span>hello@brightwellrooms.com</span></div>
<div class="abs social"><i></i><i></i><i></i></div>

<h4 class="abs foot-h" style="left:490px">LOCATION</h4>
<div class="abs map" role="img" aria-label="Street map showing the showroom location"></div>

<h4 class="abs foot-h" style="left:875px">SITE MAP</h4>
<ul class="abs sitemap">
  <li>HOME</li><li>SUNROOMS</li><li>SHADE SOLUTIONS</li><li>OPTIONS &amp; ACCESSORIES</li><li>ABOUT US</li>
</ul>

<div class="abs bottom"></div>
<p class="abs copy">© 2020 <b>BRIGHTWELL ROOMS</b> - ALL RIGHTS RESERVED</p>
<svg class="abs to-top" viewBox="0 0 36 36"><path d="M11 21 L18 14 L25 21" fill="none" stroke="#9a9a9a" stroke-width="2"/></svg>

</body>
</html>
```